Realtor business card

Looking for a business card that will stand out from the rest. My area of expertise is residential real estate and loans.

Industry/Entity Type

Residential

Requirements
Must have
• Marcus Whitley, SFR
Broker
Mortgage Loan Originator
Notary Public
DRE License #07329184
NMLS 581706
Cell 714-552-0718
Fax 888-417-2965
www.marcuswhitleyhomes.example
mw@marcuswhitleyhomes.example

```html
<!DOCTYPE html>
<html lang="en">
<head>
<meta charset="utf-8">
<title>Marcus Whitley — Business Card</title>
<link rel="stylesheet" href="https://fonts.googleapis.com/css2?family=Roboto:wght@300;400;700&display=swap">
<style>
  :root {
    --page-bg: #e6e6e6;
    --card-top: #0aaadd;
    --card-bottom: #078fc3;
    --panel: #0a86b9;
    --panel-shadow: rgba(0, 40, 70, 0.35);
    --ink: #ffffff;
  }
  * { margin: 0; padding: 0; box-sizing: border-box; }
  html, body {
    width: 1200px;
    height: 1000px;
    overflow: hidden;
    background: var(--page-bg);
    font-family: "Roboto", "Helvetica Neue", Arial, sans-serif;
    color: var(--ink);
  }
  .canvas { position: relative; width: 1200px; height: 1000px; }

  .card {
    position: absolute;
    overflow: hidden;
    background: linear-gradient(to bottom, var(--card-top), var(--card-bottom));
  }
  .card--front { left: 302px; top: 118px; width: 603px; height: 348px; }
  .card--back  { left: 302px; top: 530px; width: 605px; height: 350px; }

  .panel {
    position: absolute;
    background: var(--panel);
    box-shadow: 0 2px 5px var(--panel-shadow);
  }
  .card--front .panel { left: 299px; top: 115px; width: 304px; height: 118px; }
  .card--back .panel  { left: 0; top: 115px; width: 302px; height: 118px; }

  .website {
    position: absolute;
    font-size: 15px;
    font-weight: 400;
    letter-spacing: 0.4px;
    white-space: nowrap;
    transform: translate(-50%, -50%);
  }
  .card--front .website { left: 151px; top: 174px; }
  .card--back .website  { left: 445px; top: 175px; }

  .name {
    position: absolute;
    left: 40px;
    top: 24px;
    font-size: 25px;
    font-weight: 300;
    letter-spacing: 0.2px;
    white-space: nowrap;
  }
  .rule {
    position: absolute;
    height: 2px;
    background: var(--ink);
  }
  .card--front .rule { left: 40px; top: 58px; right: 0; }
  .card--back .rule  { left: 0; top: 59px; width: 65px; }

  .titles {
    position: absolute;
    left: 40px;
    top: 64px;
    font-size: 8.5px;
    white-space: nowrap;
  }

  .contact {
    position: absolute;
    right: 38px;
    top: 34px;
    text-align: right;
    font-size: 12px;
    line-height: 17px;
    list-style: none;
  }
  .contact strong { font-weight: 700; }

  .licenses {
    position: absolute;
    left: 86px;
    top: 250px;
    font-size: 12px;
    white-space: nowrap;
  }
</style>
</head>
<body>
  <main class="canvas">
    <section class="card card--front" aria-label="Card front">
      <p class="website">www.marcuswhitleyhomes.example</p>
      <div class="panel">
        <h1 class="name">Marcus Whitley</h1>
        <div class="rule"></div>
        <p class="titles">SFR Broker \ Mortgage Loan Originator \ Notary Public</p>
      </div>
    </section>

    <section class="card card--back" aria-label="Card back">
      <div class="panel">
        <div class="rule"></div>
        <ul class="contact">
          <li><strong>Cell</strong>: 714-552-0718</li>
          <li><strong>Fax</strong>: 888-417-2965</li>
          <li><strong>E-mail</strong>: mw@marcuswhitleyhomes.example</li>
        </ul>
      </div>
      <p class="licenses">DRE License #07329184 \ NMLS 581706</p>
      <p class="website">www.marcuswhitleyhomes.example</p>
    </section>
  </main>
</body>
</html>
```